The Willow Nest

a business card that we will give to customers, Doctors, Midwifes, surgeons, Pilates and Yoga instructors, chiropractors, physiotherapists.
Our business is based in Australia, Melbourne

Please visit our website to get a better idea about our business www.thewillownest.com.au
Updates

Target Market(s)

health, wellbeing, no surgery, natural healing, medical

Industry/Entity Type

Business

Contact Information for Business Card

Mira Holcott
Pilates Instructor
0412 608 271

Rosalind Garrick
Yoga Instructor
0409 375 516

email thewillownest@quillmail.com
Website www.thewillownest.com.au

Requirements
Must have
• A classy, sophisticated feel.

front and back
Use of our business Logo (either in black or white)
Use of Varenko Method Logo - this logo must be smaller then our business logo as it is just a contractual legal requirement to have this logo

NOTE: we could not upload more files as this would only let us upload one file - please contact us for the other logo's.
Nice to have
• targeted at both female and male.

Different base colours on each side

our business is about repairing separated abdominals:
Do you have a Bulging belly?
Do you get asked if you are pregnant?
Have been diagnosed with a Diastasis Recti?
Do you Suffer back pain or hip pain?
Weak core strength and weak pelvic floor?
Considering a tummy tuck? (it can be healed without surgery)
Have an umbilical hernia?
An "Outie" belly button that used to be an "Innie"?
Plus we specialise in Pilates and yoga

```html
<!DOCTYPE html>
<html lang="en">
<head>
<meta charset="utf-8">
<title>The Willow Nest – Business Card</title>
<link href="https://fonts.googleapis.com/css2?family=Open+Sans:ital,wght@0,400;0,600;1,400&display=swap" rel="stylesheet">
<style>
  :root {
    --backdrop: #3a3a3a;
    --card-front-top: #2e2e2e;
    --card-front-bottom: #121212;
    --card-back-top: #0c0c0c;
    --card-back-bottom: #3c3c3c;
    --brand-blue: #7cc8e8;
    --text-light: #f2f2f2;
    --text-muted: #b5b5b5;
    --accent-red: #e2382f;
  }
  html, body {
    margin: 0;
    width: 1200px;
    height: 900px;
    overflow: hidden;
    background: var(--backdrop);
    font-family: "Open Sans", Arial, sans-serif;
  }
  .canvas { position: relative; width: 1200px; height: 900px; }
  .card {
    position: absolute;
    top: 293px;
    width: 515px;
    height: 315px;
    box-shadow: 0 4px 14px rgba(0,0,0,.55);
    overflow: hidden;
    color: var(--text-light);
  }
  .card--front {
    left: 72px;
    background: linear-gradient(180deg, var(--card-front-top), var(--card-front-bottom));
    text-align: center;
  }
  .card--back {
    left: 615px;
    background: linear-gradient(180deg, var(--card-back-top) 0%, #1c1c1c 50%, var(--card-back-bottom) 100%);
  }
  .brand { position: absolute; }
  .brand__name {
    display: flex; align-items: center; gap: 8px;
    font-size: 27px; font-weight: 400; color: var(--brand-blue);
    letter-spacing: .5px; line-height: 1;
  }
  .brand__dot {
    width: 12px; height: 12px; border-radius: 50%;
    background: var(--accent-red); flex: none;
  }
  .brand__tagline {
    font-size: 9.5px; color: var(--text-muted); letter-spacing: .8px;
    text-align: right; margin-top: 5px;
  }
  .card--front .brand { left: 130px; top: 42px; }
  .holder__name { position: absolute; top: 118px; left: 0; right: 0; font-size: 25px; }
  .holder__role { position: absolute; top: 151px; left: 0; right: 0; font-size: 14px; color: var(--text-muted); }
  .contact { position: absolute; top: 183px; left: 0; right: 0; font-size: 14.5px; line-height: 21px; }
  .contact__item { display: flex; justify-content: center; align-items: center; gap: 4px; }
  .contact__item svg { width: 11px; height: 11px; fill: var(--text-light); }
  .partner {
    position: absolute; top: 276px; left: 0; right: 0;
    font-size: 12px; color: var(--text-light);
  }
  .tape-visual {
    position: absolute; left: 0; top: 0; width: 170px; height: 315px;
    background: linear-gradient(100deg, rgba(200,200,200,.35), rgba(120,120,120,.12) 70%, rgba(0,0,0,0));
  }
  .card--back .brand { left: 198px; top: 40px; }
  .concerns {
    position: absolute; left: 206px; top: 100px; margin: 0; padding: 0;
    list-style: none; font-style: italic; font-size: 12.3px; line-height: 19.6px;
    color: var(--text-light);
  }
  .concerns li::before { content: "• "; font-style: normal; }
  .concerns .note { display: block; padding-left: 9px; line-height: 13px; margin-bottom: 4px; }
</style>
</head>
<body>
<main class="canvas">
  <section class="card card--front">
    <div class="brand">
      <div class="brand__name"><span class="brand__dot"></span>The Willow Nest</div>
      <div class="brand__tagline">ABDOMINAL REHABILITATION</div>
    </div>
    <div class="holder__name">Mira Holcott</div>
    <div class="holder__role">PILATES INSTRUCTOR</div>
    <div class="contact">
      <div class="contact__item">
        <svg viewBox="0 0 12 12"><path d="M2.5 1l2 2.2-1 1.3a7 7 0 0 0 4 4l1.3-1 2.2 2-1.3 1.5C5 11 1 7 1 2.3z"/></svg>
        0412 608 271
      </div>
      <div class="contact__item">
        <svg viewBox="0 0 12 12"><path d="M1 3h10v6H1z M1 3l5 3.5L11 3" fill="none" stroke="#f2f2f2" stroke-width="1.2"/></svg>
        thewillownest@quillmail.com
      </div>
      <div class="contact__item">
        <svg viewBox="0 0 12 12"><g fill="none" stroke="#f2f2f2" stroke-width="1"><circle cx="6" cy="6" r="5"/><ellipse cx="6" cy="6" rx="2.2" ry="5"/><path d="M1 6h10"/></g></svg>
        www.thewillownest.com.au
      </div>
    </div>
    <div class="partner">Varenko Method</div>
  </section>

  <section class="card card--back">
    <div class="tape-visual" role="img" aria-label="Curling measuring tape decoration"></div>
    <div class="brand">
      <div class="brand__name"><span class="brand__dot"></span>The Willow Nest</div>
      <div class="brand__tagline">ABDOMINAL REHABILITATION</div>
    </div>
    <ul class="concerns">
      <li>Do you have a Bulging belly?</li>
      <li>Do you get asked if you are pregnant?</li>
      <li>Have been diagnosed with a Diastasis Recti?</li>
      <li>Do you Suffer back pain or hip pain?</li>
      <li>Weak core strength and weak pelvic floor?</li>
      <li>Considering a tummy tuck?<span class="note">(it can be healed without surgery)</span></li>
      <li>Have an umbilical hernia?</li>
      <li>An "Outie" belly button that used to be an "Innie"?</li>
      <li>Plus we specialise in Pilates and yoga</li>
    </ul>
  </section>
</main>
</body>
</html>
```